Business Card Design

I would like a new business card design for an accounting firm that specializes in resolving clients tax problems. I want the card to give the impression that we are not your typical stodgy accounting firm, but at the same time we will get the job done.
Industry/Entity Type
Business
Contact Information for Business Card
Dorian T Welsby
Certified Public Accountant
38-27 52nd Street
Sunnyside, NY 11287
Tel: (718) 555-0142
Fax: (888) 555-0199
e-mail: dtwthecpa@ledgerpost.com
website: harborfilingreliefexperts.com

```html
<!DOCTYPE html>
<html lang="en">
<head>
<meta charset="utf-8">
<title>Dorian T Welsby — Business Card</title>
<link rel="stylesheet" href="https://fonts.googleapis.com/css2?family=Bebas+Neue&display=swap">
<style>
  :root {
    --backdrop: #2a2c31;
    --card-red: #8f1f1f;
    --card-red-light: #9b2523;
    --ink-white: #ffffff;
    --ink-grey: #5d5f62;
    --icon-white: #f4f4f4;
  }
  * { margin: 0; padding: 0; box-sizing: border-box; }
  html, body {
    width: 1200px;
    height: 900px;
    overflow: hidden;
    background: var(--backdrop);
  }
  body { position: relative; font-family: "Bebas Neue", "Arial Narrow", sans-serif; }

  .business-card {
    position: absolute;
    left: 100px;
    top: 164px;
    width: 1000px;
    height: 572px;
    background: radial-gradient(ellipse at 45% 40%, var(--card-red-light), var(--card-red) 75%);
    box-shadow: 0 18px 40px rgba(0,0,0,0.45);
  }

  .identity { position: absolute; left: 70px; top: 262px; }
  .identity__name {
    color: var(--ink-white);
    font-size: 92px;
    line-height: 0.9;
    letter-spacing: 1px;
    display: inline-block;
    padding-bottom: 6px;
    border-bottom: 6px solid var(--ink-white);
  }
  .identity__title {
    color: var(--ink-grey);
    font-size: 50px;
    line-height: 1;
    letter-spacing: 0.5px;
    margin-top: 8px;
  }

  .contact { position: absolute; display: flex; align-items: center; gap: 14px; }
  .contact__icon { flex: none; }
  .contact__lines { color: var(--ink-grey); text-transform: uppercase; }
  .contact__lines p { line-height: 1.15; }

  .contact--online { left: 560px; top: 60px; }
  .contact--online .contact__icons { display: flex; flex-direction: column; gap: 10px; }
  .contact--online .contact__lines { font-size: 29px; }

  .contact--phone { left: 600px; top: 196px; }
  .contact--phone .contact__lines { font-size: 36px; }

  .contact--address { left: 650px; top: 322px; }
  .contact--address .contact__lines { font-size: 36px; }
</style>
</head>
<body>
  <section class="business-card">
    <div class="contact contact--online">
      <div class="contact__icons">
        <svg class="contact__icon" width="46" height="34" viewBox="0 0 46 34" aria-hidden="true">
          <rect x="2" y="8" width="42" height="24" fill="none" stroke="var(--icon-white)" stroke-width="3"/>
          <polyline points="2,8 23,23 44,8" fill="none" stroke="var(--icon-white)" stroke-width="3"/>
          <circle cx="23" cy="9" r="6" fill="none" stroke="var(--icon-white)" stroke-width="2.5"/>
        </svg>
        <svg class="contact__icon" width="46" height="34" viewBox="0 0 46 34" aria-hidden="true">
          <rect x="2" y="2" width="42" height="30" rx="3" fill="none" stroke="var(--icon-white)" stroke-width="3"/>
          <rect x="7" y="7" width="32" height="20" fill="none" stroke="var(--icon-white)" stroke-width="1.5"/>
        </svg>
      </div>
      <div class="contact__lines">
        <p>dtwthecpa@ledgerpost.com</p>
        <p>harborfilingreliefexperts.com</p>
      </div>
    </div>

    <div class="contact contact--phone">
      <svg class="contact__icon" width="34" height="70" viewBox="0 0 34 70" aria-hidden="true">
        <path d="M14 4 L24 6 L22 20 L16 22 Q12 35 16 48 L22 50 L24 64 L14 66 Q2 52 2 35 Q2 18 14 4 Z" fill="var(--icon-white)"/>
      </svg>
      <div class="contact__lines">
        <p>Tel: (718) 555-0142</p>
        <p>Fax: (888) 555-0199</p>
      </div>
    </div>

    <div class="contact contact--address">
      <svg class="contact__icon" width="44" height="62" viewBox="0 0 44 62" aria-hidden="true">
        <path d="M22 2 C10 2 2 11 2 22 C2 36 22 60 22 60 C22 60 42 36 42 22 C42 11 34 2 22 2 Z" fill="var(--icon-white)"/>
        <circle cx="22" cy="21" r="8" fill="none" stroke="var(--card-red)" stroke-width="4"/>
      </svg>
      <div class="contact__lines">
        <p>38-27 52nd Street</p>
        <p>Sunnyside, NY 11287</p>
      </div>
    </div>

    <div class="identity">
      <h1 class="identity__name">DORIAN T WELSBY</h1>
      <p class="identity__title">CERTIFIED PUBLIC ACCOUNTANT</p>
    </div>
  </section>
</body>
</html>
```